Web Design Project - Event Management Company

A web-page design needs to be created for an event management company. The logo has already been created, the design needs to draw on the themes and colors of the logo and extend on that.

The event management company likes to differentiate itself from others by being a bit "un-conventional" and being able to think outside the box.

the specialise in corporate events, weddings, AGMs, anything that requires coordination of resources. They also can provide Audio Visual services such as recording events.

final design will also require HTML implementation

```html
<!DOCTYPE html>
<html lang="en">
<head>
<meta charset="utf-8">
<title>Odd Block Events</title>
<link rel="stylesheet" href="https://fonts.googleapis.com/css2?family=PT+Sans:wght@400;700&family=PT+Sans+Narrow:wght@700&family=Roboto+Condensed:wght@400;700&family=Arimo&display=swap">
<style>
:root{
  --page:#f8e1df;
  --dark:#5b504e;
  --dark-deep:#4b413f;
  --orange:#e2541f;
  --pink:#f0708f;
  --pink-line:#f08aa4;
  --white:#ffffff;
  --text:#2b2523;
  --body:#3a3432;
  --photo-warm:#c9a07a;
  --photo-green:#7d8f5a;
}
*{box-sizing:border-box;margin:0;padding:0}
html,body{width:927px;height:1200px;overflow:hidden}
body{position:relative;background:var(--page);font-family:"PT Sans",sans-serif;color:var(--text)}
.abs{position:absolute}
.top-rule{left:0;top:0;width:927px;height:3px;background:var(--dark)}
.account-tab{left:668px;top:3px;width:140px;height:22px;background:var(--dark);clip-path:polygon(0 0,100% 0,92% 100%,6% 100%);color:var(--white);font:700 11px "PT Sans",sans-serif;display:flex;align-items:center;justify-content:center;gap:8px}
.brand{left:120px;top:30px;display:flex;align-items:center;gap:8px;font:700 20px "Roboto Condensed",sans-serif;color:var(--dark);letter-spacing:.5px}
.brand-mark{width:30px;height:30px;background:var(--orange)}
.phone{right:126px;top:63px;font:700 15px "PT Sans",sans-serif;color:#6b605e}
.nav{left:118px;top:112px;width:690px;height:50px;background:var(--dark);border-radius:12px 12px 0 0;display:flex;align-items:flex-start}
.nav a{color:var(--white);text-decoration:none;font:700 9px "PT Sans",sans-serif;height:38px;display:flex;align-items:center;justify-content:center}
.nav .home{background:var(--orange);font-size:11px;width:74px;margin-left:22px}
.nav .about{font-size:11px;width:104px}
.hero{left:118px;top:150px;width:690px;height:274px;background:var(--white);border-radius:14px;border:0}
.hero-wrap{left:118px;top:150px;width:690px;height:286px;background:var(--dark);border-radius:0 0 10px 10px}
.shot{position:absolute}
.card{width:223px;height:112px;top:424px;background:var(--dark);border-radius:0 0 16px 16px}
.card .shot{left:8px;top:10px;width:207px;height:73px;border:2px solid var(--white);border-radius:6px}
.card span{position:absolute;left:0;right:0;top:86px;text-align:center;color:var(--white);font:700 13px "PT Sans",sans-serif}
.sec-title{font:700 15px "Roboto Condensed",sans-serif;color:var(--pink)}
.sec-rule{height:2px;background:linear-gradient(90deg,var(--dark) 0 30%,var(--orange) 30%)}
.video{left:134px;top:617px;width:413px;height:265px;background:linear-gradient(160deg,#6d1c1c,#b8303a 50%,#3d1214)}
.video-bar{left:0;top:0;width:100%;height:41px;background:linear-gradient(#3a2a2a,#5a3030);color:var(--white);font:400 19px "PT Sans",sans-serif;padding:9px 10px}
.video-badge{right:14px;top:8px;width:26px;height:24px;background:var(--orange)}
.controls{left:0;bottom:0;width:100%;height:18px;background:#e8e6e6;display:flex;align-items:center;gap:6px;padding:0 4px;font:700 8px "PT Sans",sans-serif;color:var(--text)}
.track{flex:1;height:4px;background:#bdbaba;border-radius:2px}
.lead{left:134px;top:896px;font:700 14.5px "PT Sans",sans-serif}
.copy{left:134px;top:925px;width:440px;font:10px/17.6px Arimo,sans-serif;color:var(--body)}
.copy p+p{margin-top:4px}
.panel{background:var(--white)}
.quote{position:absolute;left:11px;display:flex;gap:12px;font:8px/16.5px "PT Sans",sans-serif;color:var(--text)}
.quote .face{width:48px;height:45px;flex:none;background:linear-gradient(135deg,#e9c9a8,#b98860)}
.field{position:absolute;left:10px;width:206px;height:20px;border:1.5px solid var(--pink-line);background:var(--white);font:10px "PT Sans",sans-serif;color:#555;padding:3px 9px}
.submit{left:630px;top:1006px;width:132px;height:32px;background:var(--orange);border-radius:16px;box-shadow:2px 2px 0 #4d7a2a;color:var(--white);font:700 15px "Roboto Condensed",sans-serif;display:flex;align-items:center;justify-content:center}
.footer{left:0;top:1058px;width:927px;height:142px;background:var(--dark)}
.foot-head{color:var(--white);font:700 12px "PT Sans",sans-serif}
.foot-list{list-style:none;font:700 9px/16px "PT Sans Narrow",sans-serif;color:var(--white)}
.foot-list li::before{content:"»";margin-right:7px;color:#ccc}
.divider{top:1075px;width:2px;height:110px;background:linear-gradient(#5b504e,#3f3634,#5b504e)}
.news-input{left:609px;top:1093px;width:196px;height:19px;background:var(--white);border-radius:3px;font:8px "PT Sans",sans-serif;padding:4px 6px;color:#333}
.news-btn{left:608px;top:1119px;width:70px;height:20px;background:var(--orange);border-radius:3px;color:var(--white);font:700 9px "PT Sans",sans-serif;display:flex;align-items:center;justify-content:center}
.social{display:flex;gap:12px;align-items:center}
.social i{display:block;width:15px;height:15px;border-radius:3px}
.copyright{left:610px;top:1173px;color:var(--white);font:8px "PT Sans",sans-serif}
</style>
</head>
<body>
<div class="abs top-rule"></div>
<div class="abs account-tab"><span>SIGN UP</span><span>|</span><span>LOGIN</span></div>

<div class="abs brand"><span class="brand-mark"></span>ODD BLOCK EVENTS</div>
<div class="abs phone">Phone: (00) 55501-24680</div>

<nav class="abs nav">
  <a class="home" href="#">HOME</a>
  <a class="about" href="#">ABOUT US</a>
  <a href="#" style="width:80px">CORPORATE</a>
  <a href="#" style="width:84px">SOCIAL</a>
  <a href="#" style="width:92px">WEDDINGS</a>
  <a href="#" style="width:92px">PORTFOLIO</a>
  <a href="#" style="width:108px">CONTACT US</a>
</nav>

<div class="abs hero-wrap"></div>
<section class="abs hero">
  <div class="shot" role="img" aria-label="Banquet hall with chandelier and dining tables" style="left:4px;top:4px;width:91px;height:266px;background:linear-gradient(#e6cf9c,#b89060);border-radius:10px 0 0 0"></div>
  <div class="shot" role="img" aria-label="Bride and groom in front of a stone mansion" style="left:98px;top:4px;width:86px;height:266px;background:linear-gradient(#cbb897,#8f7f68)"></div>
  <div class="shot" role="img" aria-label="Hands holding an autumn bridal bouquet" style="left:187px;top:4px;width:85px;height:266px;background:linear-gradient(#e9e2d6,#c46a3c 45%,#6c7a3a)"></div>
  <div class="shot" role="img" aria-label="Bride with bridesmaids holding yellow bouquets on a lawn" style="left:274px;top:4px;width:411px;height:266px;background:linear-gradient(#4f6b3a,#e0a58a 40%,#a9a3a0 70%,#5d7a3b);border-radius:0 10px 0 0"></div>
</section>

<div class="abs card" style="left:118px"><div class="shot" role="img" aria-label="Business team meeting in an office" style="background:linear-gradient(#9fb6cf,#4c6a8c)"></div><span>CORPORATE EVENTS</span></div>
<div class="abs card" style="left:350px"><div class="shot" role="img" aria-label="Friends celebrating at a party with confetti" style="background:linear-gradient(#7b6a63,#c09a86)"></div><span>SOCIAL EVENTS</span></div>
<div class="abs card" style="left:585px"><div class="shot" role="img" aria-label="Bride walking with bridesmaids in a garden" style="background:linear-gradient(#6f8a55,#d7d3cc)"></div><span>WEDDING EVENTS</span></div>

<div class="abs" style="left:122px;top:566px;width:28px;height:28px;background:var(--orange)"></div>
<h2 class="abs sec-title" style="left:168px;top:577px">COMPLETE EVENT MANAGEMENT</h2>
<div class="abs sec-rule" style="left:118px;top:600px;width:458px"></div>

<div class="abs video" role="img" aria-label="Video of a ballroom event with guests under red lighting">
  <div class="abs video-bar">Event Management</div>
  <div class="abs video-badge"></div>
  <div class="abs controls">
    <svg width="8" height="8"><path d="M1 0L8 4L1 8Z" fill="#222"/></svg>
    <svg width="7" height="7"><rect width="7" height="7" fill="#222"/></svg>
    <span>00:00</span><div class="track"></div><span>00:00</span>
    <svg width="9" height="9"><rect x=".5" y=".5" width="8" height="8" fill="none" stroke="#222"/></svg>
    <svg width="18" height="8"><path d="M0 3h3l3-3v8l-3-3H0Z M9 6v2M11 5v3M13 3v5M15 2v6M17 0v8" stroke="#222" fill="#222"/></svg>
  </div>
</div>

<h3 class="abs lead">Lorem ipsum dolor sit amet, consectetuer adipiscing</h3>
<div class="abs copy">
  <p>Lorem ipsum dolor sit amet, consectetuer adipiscing elit, sed diam nonummy nibh euismod tincidunt ut laoreet dolore magna aliquam erat volutpat. Ut wisi enim ad minim veniam, quis nostrud exerci tation ullamcorper suscipit lobortis nisl ut aliquip ex ea commodo consequat.</p>
  <p>Lorem ipsum dolor sit amet, consectetuer adipiscing elit, sed diam nonummy nibh euismod tincidunt ut laoreet dolore magna aliquam erat volutpat. Ut wisi enim ad minim veniam, quis nostrud exerci tation ullamcorper suscipit lobortis nisl ut aliquip ex ea commodo consequat.</p>
</div>

<h2 class="abs sec-title" style="left:583px;top:578px">CLIENT &nbsp;TESTIMONIALS</h2>
<div class="abs sec-rule" style="left:582px;top:600px;width:227px;background:var(--orange)"></div>
<section class="abs panel" style="left:583px;top:602px;width:226px;height:196px">
  <div class="quote" style="top:12px"><div class="face" role="img" aria-label="Client portrait"></div><p>Lorem ipsum dolor sit amet, consect etuer adipiscing elit, sed diam nonummy nibh euism...</p></div>
  <div class="quote" style="top:76px"><div class="face" role="img" aria-label="Client portrait"></div><p>Lorem ipsum dolor sit amet, consect etuer adipiscing elit, sed diam nonummy nibh euism...</p></div>
  <div class="quote" style="top:138px"><div class="face" role="img" aria-label="Client portrait"></div><p>Lorem ipsum dolor sit amet, consect etuer adipiscing elit, sed diam nonummy nibh euism...</p></div>
</section>

<h2 class="abs sec-title" style="left:592px;top:824px">QUICK CONTACT</h2>
<div class="abs sec-rule" style="left:582px;top:847px;width:227px;background:var(--orange)"></div>
<section class="abs panel" style="left:583px;top:849px;width:226px;height:199px">
  <div class="field" style="top:19px">Full Name</div>
  <div class="field" style="top:44px">Email Address</div>
  <div class="field" style="top:68px">Phone</div>
  <div class="field" style="top:93px;height:56px">Comments</div>
</section>
<div class="abs submit">SUBMIT</div>

<footer class="abs footer"></footer>
<div class="abs divider" style="left:257px"></div>
<div class="abs divider" style="left:557px"></div>

<h4 class="abs foot-head" style="left:120px;top:1071px">OUR SERVICES</h4>
<ul class="abs foot-list" style="left:122px;top:1092px">
  <li>Corporate Events</li><li>Social Events</li><li>Wedding Events</li><li>Birtday Events</li><li>Stage Events</li>
</ul>

<h4 class="abs foot-head" style="left:300px;top:1071px">QUICK LINKS</h4>
<ul class="abs foot-list" style="left:303px;top:1091px">
  <li>Home</li><li>About Us</li><li>CORPORATE</li><li>PORTFOLIO</li><li>CONTACT US</li>
</ul>
<ul class="abs foot-list" style="left:423px;top:1091px">
  <li>Wedding Packages</li><li>Advanced Search</li><li>Contact Us</li><li>SOCIAL</li><li>Terms &amp; Conditions</li><li>Privacy Policy</li>
</ul>

<h4 class="abs foot-head" style="left:609px;top:1071px">NEWSLETTER SUBSCRIPTION</h4>
<div class="abs news-input">--Enter your Email Address--</div>
<div class="abs news-btn">SUBSCRIBE</div>
<div class="abs social" style="left:609px;top:1149px">
  <span class="foot-head">FOLLOW US</span>
  <i style="background:#3b5998"></i><i style="background:#3aa6d8"></i><i style="background:#1c7fb8"></i><i style="background:#ffffff"></i><i style="background:#d32a3a"></i>
</div>
<div class="abs copyright">Copyright @ 2013 EventHarbor.com</div>
</body>
</html>
```